Holistic Psychologist needs contemporary business card

I am a psychologist working with adult clients face to face and online. The card needs to work for clients and also referring doctors and medical professionals. It needs to look warm, safe and trustable for clients, but clean and professional enough for doctors. Sometimes I also work in a corporate context.

I am holistic in my approach (mind-body-spirit) so anything conveying connection or integration or wholeness would be good. But again, clean and contemporary please. It can have a little bit of personality.
New logo uploaded.

Probably warm tones and plenty white space to write on one side.

My web pages:
http://lmtherapy.com.au
https://www.facebook.com/MarcellaWhitfordTherapy?ref=hl
Updates

Hi Designers .. I have decided I do need a new logo before finalising a design for the business cards.  I hope to have this available in 4 days from now.

Kindly,

Marcella

New logo now posted, same brief.  Balance of masculine and feminine elements, plenty of white space on one side please.

Keen to see some card designs, thank-you.

Target Market(s)

Audience 1 - Males and females aged 25 years + seeking counselling or coaching. Audience 2 - doctors and health professionals who refer clients.

Industry/Entity Type

Medical

Contact Information for Business Card

Logo

Marcella Whitford
Registered Psychologist

M: 0491 508 243
www.lmtherapy.com.au
marcella@lmtherapy.com.au
Little blue Facebook icon, with "marcella whitford therapy" printed near it.

Font styles to use
Sans Serif

Requirements
Nice to have
• You might want to play with the words "Balanced Self"
Should not have
• Nothing cutesy or too literal

```html
<!DOCTYPE html>
<html lang="en">
<head>
<meta charset="utf-8">
<title>Marcella Whitford Psychology – Business Card</title>
<link rel="stylesheet" href="https://fonts.googleapis.com/css2?family=Didact+Gothic&display=swap">
<style>
  :root {
    --stage: #9a9a9a;
    --card-white: #ffffff;
    --brand-red: #e3202a;
    --ink: #1a1a1a;
    --panel-top: #2a2b2d;
    --panel-bottom: #0b0b0c;
    --contact-text: #ffffff;
    --watermark-peach: #f6d3c4;
    --watermark-grey: #cfcaca;
  }
  * { box-sizing: border-box; margin: 0; padding: 0; }
  html, body {
    width: 1200px; height: 900px; overflow: hidden;
    background: var(--stage);
    font-family: "Didact Gothic", "Century Gothic", sans-serif;
  }
  .stage {
    position: relative; width: 1200px; height: 900px;
    display: flex; justify-content: center; align-items: center; gap: 12px;
  }
  .card {
    position: relative; width: 592px; height: 364px;
    background: var(--card-white); overflow: hidden;
  }

  /* Front */
  .front__header {
    height: 189px; display: flex; align-items: center;
    padding-left: 60px; gap: 38px;
  }
  .brand-dot {
    width: 84px; height: 84px; border-radius: 50%;
    background: var(--brand-red); flex: none;
  }
  .brand-name {
    color: var(--brand-red); font-size: 44px; font-weight: 400;
    line-height: 1; white-space: nowrap;
  }
  .brand-discipline {
    margin-top: 10px; color: var(--ink); font-size: 20px; line-height: 1;
    letter-spacing: 16.6px; white-space: nowrap;
  }
  .tagline-band {
    height: 16px; background: var(--brand-red);
    display: flex; justify-content: space-between; align-items: center;
    padding: 0 52px 0 66px;
    font-size: 12px; color: var(--ink); line-height: 1;
  }
  .front__contact {
    height: 159px;
    background: linear-gradient(180deg, var(--panel-top) 0%, var(--panel-bottom) 100%);
    padding: 27px 0 0 36px;
    list-style: none;
  }
  .contact-item {
    display: flex; align-items: center; gap: 6px;
    color: var(--contact-text); font-size: 19px; line-height: 24px;
    white-space: nowrap;
  }
  .contact-icon { width: 20px; height: 20px; flex: none; }

  /* Back */
  .back { display: flex; align-items: center; justify-content: center; gap: 22px; }
  .back__dot {
    width: 150px; height: 150px; border-radius: 50%;
    background: var(--watermark-grey); flex: none;
  }
  .back__name {
    color: var(--watermark-peach); font-size: 58px; line-height: 1.05;
  }
</style>
</head>
<body>
<main class="stage">
  <section class="card front" aria-label="Card front">
    <header class="front__header">
      <span class="brand-dot" aria-hidden="true"></span>
      <div class="brand-text">
        <h1 class="brand-name">Marcella Whitford</h1>
        <p class="brand-discipline">PSYCHOLOGY</p>
      </div>
    </header>
    <div class="tagline-band" aria-label="Balanced self">
      <span>B</span><span>A</span><span>L</span><span>A</span><span>N</span><span>C</span><span>E</span><span>D</span>
      <span>&nbsp;</span><span>&nbsp;</span>
      <span>S</span><span>E</span><span>L</span><span>F</span>
    </div>
    <ul class="front__contact">
      <li class="contact-item">
        <svg class="contact-icon" viewBox="0 0 20 20" aria-hidden="true">
          <rect x="5" y="2" width="10" height="16" rx="1.5" fill="var(--brand-red)"/>
          <rect x="7" y="4" width="6" height="6" fill="var(--panel-bottom)"/>
          <rect x="7" y="12" width="6" height="4" fill="var(--panel-bottom)" opacity=".6"/>
        </svg>
        0491 508 243
      </li>
      <li class="contact-item">
        <svg class="contact-icon" viewBox="0 0 20 20" aria-hidden="true" fill="none" stroke="var(--brand-red)" stroke-width="1.6">
          <circle cx="10" cy="10" r="8"/>
          <ellipse cx="10" cy="10" rx="3.5" ry="8"/>
          <line x1="2" y1="10" x2="18" y2="10"/>
          <line x1="4" y1="5.5" x2="16" y2="5.5"/>
          <line x1="4" y1="14.5" x2="16" y2="14.5"/>
        </svg>
        www.lmtherapy.com.au
      </li>
      <li class="contact-item">
        <svg class="contact-icon" viewBox="0 0 20 20" aria-hidden="true">
          <rect x="1" y="4" width="18" height="13" rx="1.5" fill="var(--brand-red)"/>
          <polyline points="2,5 10,11 18,5" fill="none" stroke="var(--panel-bottom)" stroke-width="1.6"/>
        </svg>
        marcella@lmtherapy.com.au
      </li>
      <li class="contact-item">
        <svg class="contact-icon" viewBox="0 0 20 20" aria-hidden="true">
          <rect x="2" y="2" width="16" height="16" rx="2" fill="var(--brand-red)"/>
        </svg>
        marcella whitford therapy
      </li>
    </ul>
  </section>

  <section class="card back" aria-label="Card back">
    <span class="back__dot" aria-hidden="true"></span>
    <p class="back__name">Marcella<br>Whitford</p>
  </section>
</main>
</body>
</html>
```